Information Technology Cloud Services Website

"Offer in every submission a high resolution version of your concept please. It is difficult to see of my text (sales copy) was added to your screenshot or not. It is necessary for me to provide high quality feedback."

My company provides a customizable ecosystem for Brindlewave Deskset 880 and Corvel users that includes all the technologies for organizing business processes and communications, letting my clients manage business without fear.

You can see our current site at http://www.DesksetShiftCrew.com

I currently use WordPress using the theme platform OptimizePress. If you have OptimizePress, that would be perfect, yet not required. However, I do need the finish product in WordPress for future additions and edits.

The Brand colors are Light Blue just like the logo attached.

I am in the need of graphic images on every webpage that can convey the services that my company does.

We need a refresh of our existing website that looks more 2018. We have made a mockup of the content that we want and a sample of where we want it. Nothing is set in stone, if you have better ideas of where things should go, feel free.

Here are some competitors similar sites we like - but still looking for a unique design that fits out brand

https://www.quorvatek.com/

https://www.tarnwell.com/email-migrations/deskset-880-shift-crew

https://www.gorvanta.com/solutions/mailbox-migration/

https://www.plumeridge.com/

https://www.plumeridge.com/deskset-880/

Target Market(s)

Business = IT Managers, IT Directors, IT Staff, IT Vice Presidents, Chief Information Officer

Industry/Entity Type

Information Technology

Coding

Coded - Design and coding required

Number of Pages Required

5+ page

Font styles to use
Sans Serif

Colors

Designer to choose colors to be used in the design.

Requirements
Must have
• Must have creative graphic images that convey the story/services that I offer. Its important to us that the design is very explanatory, the customer should easily be able to figure out that we provide Deskset 880 migrations services right away. Also we are looking for a new very responsive HTML5+ webpages in WordPress.

```html
<!DOCTYPE html>
<html lang="en">
<head>
<meta charset="utf-8">
<title>DesksetShiftCrew.com – Deskset 880 Migration Services</title>
<link href="https://fonts.googleapis.com/css2?family=Oswald:wght@500;700&family=Montserrat:wght@600;700&family=Open+Sans:wght@400;600;700&display=swap" rel="stylesheet">
<style>
:root{
  --blue:#29b6e8;
  --blue-deep:#1a9fd4;
  --blue-pale:#d8f1fb;
  --ink:#1e2833;
  --text:#4a5560;
  --muted:#8a949e;
  --line:#dfe5ea;
  --light:#f3f5f7;
  --white:#ffffff;
}
*{box-sizing:border-box;margin:0;padding:0}
html,body{width:1200px;height:5085px;overflow:hidden}
body{position:relative;background:var(--white);font-family:"Open Sans",Arial,sans-serif;color:var(--text)}
section,header,footer{position:absolute;left:0;width:1200px}
.abs{position:absolute}
.center{text-align:center}
.heading{font-family:"Oswald",Arial,sans-serif;font-weight:700;text-transform:uppercase;color:var(--ink);letter-spacing:.5px}
.art{position:absolute;border-radius:6px}

/* header */
.site-header{top:0;height:85px;border-bottom:1px solid var(--line)}
.brand{left:80px;top:18px;display:flex;align-items:center;gap:10px}
.brand-mark{width:44px;height:44px;border:3px solid var(--blue);border-radius:4px}
.brand-name{font-family:"Montserrat",Arial,sans-serif;font-weight:700;font-size:17px;color:var(--ink)}
.call{right:80px;top:10px;text-align:right;font-size:11px;color:var(--muted)}
.call strong{display:block;font-family:"Montserrat",Arial,sans-serif;font-size:19px;color:var(--ink)}
.main-nav{right:80px;top:58px;display:flex;gap:20px;font-size:12px;color:var(--muted)}
.main-nav span:first-child{color:var(--ink);font-weight:700}

/* hero */
.hero{top:85px;height:575px}
.hero h1{position:absolute;top:40px;left:150px;width:900px;font-family:"Montserrat",Arial,sans-serif;font-size:29px;line-height:38px;color:var(--blue);text-align:center}
.hero p{position:absolute;top:128px;width:1200px;text-align:center;font-size:15px;color:var(--text);font-weight:600}

/* migrate band */
.migrate-band{top:660px;height:355px;background:linear-gradient(180deg,var(--blue) 0%,#35c2f0 100%)}
.migrate-band .heading{position:absolute;top:70px;width:1200px;text-align:center;color:var(--white);font-size:32px}
.migrate-items{position:absolute;top:130px;left:70px;width:1060px;display:flex;justify-content:space-between}
.migrate-item{width:190px;text-align:center;color:var(--white)}
.migrate-item svg{height:80px}
.migrate-item h3{font-family:"Oswald",Arial,sans-serif;font-size:15px;text-transform:uppercase;margin-top:18px}
.migrate-item p{font-size:12px;line-height:17px;margin-top:6px;opacity:.9}

/* services */
.services{top:1015px;height:1695px}
.services>.heading{position:absolute;top:90px;width:1200px;text-align:center;font-size:32px}
.service h2{font-family:"Oswald",Arial,sans-serif;font-weight:700;text-transform:uppercase;font-size:44px;line-height:50px;color:var(--ink)}
.service .lead{font-size:14px;line-height:21px;margin-top:10px;width:430px}
.service ul{list-style:none;columns:2;column-gap:30px;margin-top:22px;font-size:12px;line-height:22px;width:520px;color:var(--ink)}
.service ul.single{columns:1}
.service li::before{content:"•";color:var(--blue);margin-right:7px}

/* about */
.about{top:2710px;height:345px;background:var(--light)}
.about .heading{position:absolute;top:50px;width:1200px;text-align:center;font-size:32px}
.about p{position:absolute;top:110px;left:160px;width:880px;text-align:center;font-size:12.5px;line-height:22px;color:var(--muted)}
.btn{display:inline-block;background:var(--blue);color:var(--white);font-family:"Montserrat",Arial,sans-serif;font-weight:700;font-size:15px;letter-spacing:1px;text-transform:uppercase;border-radius:6px}
.about .btn{position:absolute;top:245px;left:487px;width:226px;height:56px;line-height:56px;text-align:center;box-shadow:0 5px 0 var(--ink)}

/* how */
.how{top:3055px;height:570px}
.how-band{position:absolute;top:0;left:0;width:1200px;height:300px;background:linear-gradient(120deg,var(--blue) 0%,#5bcff4 60%,var(--blue-deep) 100%)}
.how .heading{position:absolute;top:110px;width:1200px;text-align:center;color:var(--white);font-size:32px}
.how-band p{position:absolute;top:165px;left:190px;width:820px;text-align:center;font-size:13px;line-height:21px;color:var(--white)}
.benefits{position:absolute;top:300px;left:0;width:1200px;height:270px;background:var(--white);display:flex;justify-content:center;gap:80px;padding-top:20px}
.benefit{width:190px;text-align:center}
.benefit .badge{width:96px;height:96px;margin:0 auto;border-radius:50%;border:3px solid var(--ink);display:flex;align-items:center;justify-content:center}
.benefit h3{font-family:"Oswald",Arial,sans-serif;font-size:16px;color:var(--ink);text-transform:uppercase;margin-top:22px}
.benefit p{font-size:12.5px;line-height:19px;margin-top:8px}

/* testimonial */
.testimonial{top:3625px;height:545px;background:linear-gradient(180deg,#f4f6f8 0%,#e4e9ee 100%)}
.testimonial .heading{position:absolute;top:60px;width:1200px;text-align:center;font-size:32px}
.quote-badge{position:absolute;top:125px;left:570px;width:60px;height:60px;border-radius:50%;background:var(--blue);color:var(--white);font-family:"Montserrat",Arial,sans-serif;font-size:40px;line-height:72px;text-align:center}
.testimonial blockquote{position:absolute;top:210px;left:190px;width:820px;text-align:center;font-size:13px;line-height:21px;font-style:italic;color:var(--text)}
.testimonial cite{position:absolute;top:305px;left:190px;font-style:normal;font-weight:700;font-size:13px;color:var(--ink)}
.portraits{position:absolute;top:360px;left:470px;display:flex;gap:22px}
.portraits div{width:80px;height:80px;border-radius:50%;border:4px solid var(--white);background:linear-gradient(135deg,#c9d4dc,#a8b6c1)}
.portraits div.active{border-color:var(--blue)}

/* process */
.process{top:4170px;height:490px}
.process .heading{position:absolute;top:40px;width:1200px;text-align:center;font-size:32px}
.process-line{position:absolute;top:210px;left:0;width:1200px;height:4px;background:var(--line)}
.step{position:absolute;top:130px;width:200px}
.step .box{height:170px;border:2px solid var(--line);background:var(--white);display:flex;align-items:center;justify-content:center}
.step.current .box{background:var(--blue);border-color:var(--blue)}
.step h3{font-family:"Oswald",Arial,sans-serif;font-size:16px;color:var(--ink);text-transform:uppercase;text-align:center;margin-top:22px}
.step p{font-size:12px;line-height:18px;text-align:center;margin-top:6px}

/* consultation */
.consult{top:4660px;height:325px;background:linear-gradient(180deg,#3bc0ee 0%,var(--blue) 100%)}
.consult .heading{position:absolute;top:55px;width:1200px;text-align:center;color:var(--white);font-size:32px}
.consult p{position:absolute;top:108px;width:1200px;text-align:center;font-size:13px;color:var(--white)}
.fields{position:absolute;top:150px;left:75px;width:1050px;display:flex;gap:14px}
.field{flex:1;height:44px;border:1px solid rgba(255,255,255,.8);border-radius:3px;background:rgba(255,255,255,.15);color:var(--white);font-size:13px;line-height:42px;padding-left:14px}
.consult .btn{position:absolute;top:235px;left:500px;width:200px;height:52px;line-height:52px;text-align:center;background:var(--white);color:var(--blue);border-radius:26px}

/* footer */
.site-footer{top:4985px;height:100px;background:var(--white)}
.site-footer .copy{position:absolute;top:42px;left:80px;font-size:12px;color:var(--muted)}
.site-footer .copy strong{color:var(--ink);font-family:"Montserrat",Arial,sans-serif}
.social{position:absolute;top:32px;right:80px;display:flex;gap:12px}
.social span{width:36px;height:36px;border-radius:50%;background:var(--blue-deep)}
.notch{position:absolute;left:580px;width:0;height:0;border-left:20px solid transparent;border-right:20px solid transparent}
</style>
</head>
<body>

<header class="site-header">
  <div class="abs brand"><span class="brand-mark"></span><span class="brand-name">DESKSETSHIFTCREW.COM</span></div>
  <div class="abs call">Call Us<strong>(877) 410-2286</strong></div>
  <nav class="abs main-nav">
    <span>Home</span><span>Email Migrations</span><span>Migration Solutions</span><span>Mergers, Acquisitions &amp; Consolidations</span><span>Services</span><span>About Us</span>
  </nav>
</header>

<section class="hero">
  <h1>Are You Willing To Cut Costs &amp; Boost Productivity By Migrating Your Email Server &amp; Infrastructure To The Cloud?</h1>
  <p>We Help Companies Quickly and Professionally Migrate To Deskset 880 &amp; Corvel...</p>
  <div class="art" role="img" aria-label="Line illustration of a hand on a tablet sending mail and documents along a cloud path to a desktop computer" style="left:110px;top:170px;width:980px;height:380px;background:linear-gradient(90deg,#eef8fd 0%,#f7fbfd 50%,#eef8fd 100%)"></div>
</section>

<section class="migrate-band">
  <span class="notch" style="top:-1px;border-top:22px solid var(--white)"></span>
  <h2 class="heading">What We Migrate</h2>
  <div class="migrate-items">
    <div class="migrate-item">
      <svg viewBox="0 0 80 80" width="80"><g fill="none" stroke="#fff" stroke-width="4"><circle cx="40" cy="26" r="12"/><path d="M16 66c0-14 10-22 24-22s24 8 24 22"/></g></svg>
      <h3>Roster Directory Synchronization</h3><p>We Need To Recreate Your Roster Directory</p>
    </div>
    <div class="migrate-item">
      <svg viewBox="0 0 90 80" width="90"><g fill="none" stroke="#fff" stroke-width="4"><rect x="8" y="16" width="74" height="50" rx="3"/><path d="M8 18l37 28 37-28"/></g></svg>
      <h3>Mailboxes</h3><p>All Email And Data From Practically All Email Platforms</p>
    </div>
    <div class="migrate-item">
      <svg viewBox="0 0 100 80" width="100"><path fill="#fff" d="M26 66a18 18 0 0 1-2-36 24 24 0 0 1 46-4 20 20 0 0 1 6 40z"/></svg>
      <h3>Data Storage</h3><p>Data Storage to OneVault Cloud Storage</p>
    </div>
    <div class="migrate-item">
      <svg viewBox="0 0 80 80" width="80"><g fill="none" stroke="#fff" stroke-width="4"><rect x="14" y="10" width="52" height="62" rx="3"/><path d="M24 28h32M24 40h32M24 52h20"/></g></svg>
      <h3>ShareDock</h3><p>From ShareDock To ShareDock Online</p>
    </div>
    <div class="migrate-item">
      <svg viewBox="0 0 80 80" width="80"><g fill="none" stroke="#fff" stroke-width="4"><rect x="14" y="12" width="52" height="56" rx="3"/><path d="M40 24v32M24 40h32"/></g></svg>
      <h3>Deskset 880 Migrations</h3><p>Migrating from one Deskset 880 tenant to another Deskset</p>
    </div>
  </div>
</section>

<section class="services">
  <h2 class="heading">Services</h2>

  <div class="abs service" style="left:80px;top:205px">
    <h2>Email Migrations</h2>
    <p class="lead">Read our case studies to find out how we able to help everyone from small business owners...</p>
    <ul>
      <li>Atrium PostBox Migration</li><li>Relaymark Migration</li><li>Gantry Suite Migration</li><li>Hybrid Configurations</li><li>Deskset 880 Migration</li><li>OpenPorter Migration</li>
      <li>Kestrel Notes Migration</li><li>IMAP</li><li>Legacy Archive Migration</li><li>Tellmoor Circle Migration</li><li>PST Migration</li><li>Zenlow Migration</li>
    </ul>
  </div>
  <div class="art" role="img" aria-label="Illustration of a laptop surrounded by email, chart and cloud icons" style="left:760px;top:150px;width:330px;height:300px;background:radial-gradient(circle,#f9d9cc 0%,#e9f6fc 70%)"></div>

  <div class="art" role="img" aria-label="Illustration of a desktop monitor with stacked document and app files" style="left:100px;top:530px;width:340px;height:300px;background:radial-gradient(circle,#dbe9f7 0%,#f4e6ef 75%)"></div>
  <div class="abs service" style="left:600px;top:555px">
    <h2>Migration Services</h2>
    <p class="lead">Read our case studies to find out how we able to help everyone from small business owners...</p>
    <ul>
      <li>Archive Migration</li><li>Corvel Migration</li><li>Document Migration</li><li>HealthCheck Relaymark/Deskset 880</li><li>Mailbox Migration</li><li>Deskset 880 Licensing Management</li>
      <li>OneVault Migration</li><li>Lookfield Configuration</li><li>Personal Archive Migration</li><li>Public Folder Migration</li><li>ShareDock Migration</li>
    </ul>
  </div>

  <div class="abs service" style="left:80px;top:935px">
    <h2>Mergers, Acquisitions &amp;<br>Consolidations</h2>
    <ul class="single">
      <li>IT Infrastructure Consulting</li><li>Deskset 880 Tenant to Tenant Migration</li><li>Project Migration Management</li><li>Enterprise Single Sign-On Solutions</li>
    </ul>
  </div>
  <div class="art" role="img" aria-label="Illustration of a person linked to devices, a rocket and a cloud" style="left:740px;top:880px;width:350px;height:330px;background:radial-gradient(circle,#fde9d2 0%,#eaf5fb 75%)"></div>

  <div class="art" role="img" aria-label="Illustration of a delivery truck carrying a laptop and servers" style="left:100px;top:1240px;width:380px;height:320px;background:radial-gradient(circle,#fbe3d4 0%,#e8f3f9 75%)"></div>
  <div class="abs service" style="left:600px;top:1395px">
    <h2>Technology Services</h2>
    <p class="lead">Read our case studies to find out how we able to help everyone from small business owners...</p>
    <ul class="single">
      <li>Enterprise Mobility</li><li>Security</li><li>Mobile Device and Application Management</li>
    </ul>
  </div>
</section>

<section class="about">
  <h2 class="heading">What We Migrate</h2>
  <p>DesksetShiftCrew will analyze your current environment and advise you of any problems. They will also prepare your Deskset 880 subscription by recreating your users and profiles to help you get ready. Then we'll do the migration. Soon DesksetShiftCrew will offer your company privacy, security software updates, document and email access control and efficiency! From synchronizing your directory to migrating your email and files, we will offer you a holistic service that will help you focus on the big picture issues.</p>
  <span class="btn">Learn More</span>
</section>

<section class="how">
  <div class="how-band">
    <h2 class="heading">How DesksetShiftCrew Can Help Your Business</h2>
    <p>When it comes to migrating your email server, apps or infrastructure to the cloud, you don't have to lose sleep or spend your budget. All you have to do is choose DesksetShiftCrew and we will professionally and efficiently handle every single detail.</p>
  </div>
  <div class="benefits">
    <div class="benefit">
      <div class="badge"><svg viewBox="0 0 50 50" width="50"><g fill="none" stroke="#1e2833" stroke-width="3"><circle cx="25" cy="25" r="19"/><path d="M25 13v12l8 6"/></g></svg></div>
      <h3>Save Time</h3><p>Our team of experts will determine your needs and develop a 100% custom migration strategy tailored to your company.</p>
    </div>
    <div class="benefit">
      <div class="badge"><svg viewBox="0 0 50 50" width="50"><g fill="none" stroke="#1e2833" stroke-width="3"><path d="M10 27l10 10 20-22"/></g></svg></div>
      <h3>Save Effort</h3><p>After identifying your needs, we will start migrating your data. Your email service will be re-routed to Deskset 880.</p>
    </div>
    <div class="benefit">
      <div class="badge"><svg viewBox="0 0 50 50" width="50"><g fill="none" stroke="#1e2833" stroke-width="3"><circle cx="25" cy="25" r="19"/><path d="M31 17h-9a4 4 0 0 0 0 8h6a4 4 0 0 1 0 8h-9M25 12v26"/></g></svg></div>
      <h3>Save Money</h3><p>Migrating your data to Deskset 880 means cutting down on expenses and boosting your performance.</p>
    </div>
  </div>
</section>

<section class="testimonial" role="img" aria-label="Faint photo of a keyboard and desk behind the testimonial">
  <h2 class="heading">Testimonial</h2>
  <div class="quote-badge">&ldquo;</div>
  <blockquote>"As a regulated company, we have all sorts of data protection requirements and industry regulations to address. Ever need to keep busy business. Deskset 880 was the only product that offered the level of security and regulatory compliance that we require. We considered other cloud based solutions, both comprehensive options and niche vendors, but nothing else could meet our compliance needs the way that Deskset 880 can."</blockquote>
  <cite>– Marla Quenby</cite>
  <div class="portraits">
    <div role="img" aria-label="Client portrait photo"></div>
    <div class="active" role="img" aria-label="Client portrait photo"></div>
    <div role="img" aria-label="Client portrait photo"></div>
  </div>
</section>

<section class="process">
  <h2 class="heading">Our Process</h2>
  <div class="process-line"></div>
  <div class="step current" style="left:75px">
    <div class="box"><svg viewBox="0 0 60 60" width="60"><g fill="none" stroke="#fff" stroke-width="3"><path d="M8 30L52 10 42 50 28 36z"/><path d="M28 36l-4 14"/></g></svg></div>
    <h3>Contact</h3><p>Our team of Experts will contact you to determine your needs and develop a custom migration strategy...</p>
  </div>
  <div class="step" style="left:370px">
    <div class="box"><svg viewBox="0 0 60 60" width="60"><g fill="none" stroke="#1e2833" stroke-width="3"><rect x="8" y="10" width="44" height="30" rx="2"/><path d="M22 50h16M30 40v10"/></g></svg></div>
    <h3>Pre-Migration</h3><p>DesksetShiftCrew will analyze your current environment and advise you of any problems...</p>
  </div>
  <div class="step" style="left:665px">
    <div class="box"><svg viewBox="0 0 60 60" width="60"><g fill="none" stroke="#1e2833" stroke-width="3"><rect x="10" y="12" width="40" height="36" rx="2"/><path d="M10 22h40M22 34h16"/></g></svg></div>
    <h3>Start Migration</h3><p>DesksetShiftCrew will start migrating your data. On your migration day the email service...</p>
  </div>
  <div class="step" style="left:960px">
    <div class="box"><svg viewBox="0 0 60 60" width="60"><g fill="none" stroke="#1e2833" stroke-width="3"><path d="M10 14h16l4 4h20v28H10z"/></g></svg></div>
    <h3>Local Setup</h3><p>We'll help you set up the new email service on local desktops, including the end-user...</p>
  </div>
</section>

<section class="consult">
  <h2 class="heading">Request A Free Consultation</h2>
  <p>Fill out the form below if you'd like to learn more or get a detailed product tour and one of our experts will reach out to you.</p>
  <div class="fields">
    <span class="field">Name*</span><span class="field">Email*</span><span class="field">Phone*</span><span class="field">Company Name*</span><span class="field">Message*</span>
  </div>
  <span class="btn">Contact Me</span>
</section>

<footer class="site-footer">
  <span class="notch" style="top:-1px;border-top:20px solid var(--blue)"></span>
  <p class="copy">2017 Copyright · <strong>DESKSETSHIFTCREW.COM</strong> · Harlow Consulting LLC</p>
  <div class="social"><span></span><span></span><span></span><span></span></div>
</footer>

</body>
</html>
```